Internet of Things integrator needs logo and website design

We need a logo and website design for our company ("Talvirex Grid"). We integrate IoT(Internet of Things) projects including: devices, network and sw solutions for all type of vertical markets. The image should be professional like the following site: quellan.io clear and easy surfing, and should include about the same sections shown in that website (Why Us?, Products, Resources, Company, etc). Website colors should follow logo colors (logo has to be designed and aproved first). The logo should be something like the one used at strevanhub.com (image attached), where we could use the logo to susbtitute the letter "o" in "IoT". The final design should communicate professionalism and experience.

Coding

Coded - Design and coding required

Number of Pages Required

5+ page

Font styles to use
Other font styles liked:
• see quellan.io wensite

Requirements
Must have
• Serious and professional look and feel as in: quellan.io website.
The following pages should be included:
- home page
- Why Us?
- Products
- Resources
- Company
- Newsroom
- Contact
Nice to have
• High tech look and feel
Should not have
• Fun or not serious images (cartoons, etc.)

```html
<!DOCTYPE html>
<html lang="en">
<head>
<meta charset="utf-8">
<title>Talvirex Grid — Industrial Edge Computing Platform</title>
<link rel="stylesheet" href="https://fonts.googleapis.com/css2?family=Oxygen:wght@300;400;700&family=Open+Sans:wght@400;600;700&display=swap">
<style>
  :root{
    --pink:#f5315c;
    --blue:#3a8cf0;
    --blue-light:#7cbcff;
    --navy:#0b1628;
    --ink:#1e2533;
    --grey:#7b8190;
    --line:#e3e6ec;
    --white:#ffffff;
  }
  *{box-sizing:border-box;margin:0;padding:0}
  html,body{width:1200px;height:3780px;overflow:hidden;background:var(--white)}
  body{position:relative;font-family:"Open Sans",Arial,sans-serif;color:var(--ink)}
  .abs{position:absolute}
  h1,h2,h3,.brand{font-family:"Oxygen","Open Sans",sans-serif}
  .eyebrow{font-size:11px;letter-spacing:1.5px;color:var(--pink);font-weight:600;text-transform:uppercase}
  .section-title{font-size:40px;font-weight:700;color:var(--ink);line-height:1.1}
  .title-rule{height:2px;width:60px;background:var(--pink);margin-top:10px}
  .title-rule.center{margin-left:auto;margin-right:auto}
  .body-text{font-size:12px;line-height:1.75;color:var(--grey)}
  .btn{display:inline-block;background:var(--pink);color:var(--white);border-radius:30px;font-weight:600;text-align:center}

  /* hero */
  .hero-photo{left:0;top:0;width:1200px;height:920px;background:linear-gradient(120deg,#0a1426 0%,#13243d 45%,#1b3150 70%,#0d1a2e 100%)}
  .hero-shade{left:0;top:0;width:1200px;height:920px;background:linear-gradient(90deg,rgba(5,10,20,.75) 0%,rgba(5,10,20,.2) 70%)}
  .nav{left:160px;top:28px;width:880px;height:40px;display:flex;align-items:center}
  .brand{color:var(--white);font-size:24px;font-weight:700;letter-spacing:1px;display:flex;align-items:center;gap:8px;white-space:nowrap}
  .brand-dot{width:12px;height:12px;border-radius:50%;background:var(--pink)}
  .nav-links{display:flex;gap:22px;margin-left:auto;margin-right:30px;font-size:12px;color:var(--white);white-space:nowrap}
  .nav-btn{padding:9px 22px;font-size:12px;white-space:nowrap}
  .hero-title{left:160px;top:348px;font-size:40px;line-height:1.2;color:var(--white);font-weight:400;letter-spacing:.5px}
  .hero-text{left:160px;top:462px;width:420px;font-size:12px;line-height:1.7;color:#dfe6f1}
  .hero-btn{left:160px;top:556px;width:230px;padding:16px 0;font-size:14px}

  /* why us */
  .why{left:0;top:880px;width:1200px;text-align:center}
  .why .body-text{width:560px;margin:20px auto 0}
  .features{left:290px;top:1130px;width:620px;display:flex;justify-content:space-between}
  .feature{width:100px;text-align:center;font-size:11px;font-weight:600;color:var(--ink);white-space:nowrap}
  .feature svg{display:block;margin:0 auto 10px}
  .why-btn{left:540px;top:1290px;width:120px;padding:10px 0;font-size:12px}

  /* resources */
  .resources-box{left:160px;top:1420px;width:300px;height:400px;background:linear-gradient(135deg,#f2f3f7 0%,#d9dce4 55%,#b9bfcc 100%);border-radius:4px}
  .resources-copy{left:610px;top:1490px;width:400px}
  .resources-copy .body-text{margin-top:22px}

  /* products */
  .products-copy{left:160px;top:1970px;width:360px}
  .products-copy .body-text{margin-top:22px}
  .product-item{display:flex;gap:18px;margin-top:34px;align-items:flex-start}
  .product-item h3{font-size:14px;font-weight:700;color:var(--ink);margin-bottom:6px}
  .product-item p{font-size:11px;line-height:1.6;color:var(--grey)}
  .products-photo{left:610px;top:1920px;width:440px;height:560px;background:linear-gradient(180deg,#2a4772 0%,#5675a0 40%,#8aa3c2 70%,#3d5370 100%);border-radius:4px}

  /* news */
  .news-head{left:0;top:2580px;width:1200px;text-align:center}
  .news-card{width:440px;height:180px;display:flex;background:var(--white);box-shadow:0 4px 18px rgba(20,30,60,.09)}
  .news-photo{width:170px;height:180px;flex:none}
  .news-body{padding:16px 18px}
  .news-date{font-size:10px;color:var(--pink);font-weight:600}
  .news-body h3{font-family:"Open Sans",sans-serif;font-size:13px;font-weight:700;margin:6px 0 8px;color:var(--ink)}
  .news-body p{font-size:10.5px;line-height:1.6;color:var(--grey)}

  /* footer */
  .footer-photo{left:0;top:3200px;width:1200px;height:580px;background:linear-gradient(160deg,#0b1830 0%,#143057 45%,#0c2144 70%,#07101f 100%)}
  .footer-shade{left:0;top:3200px;width:1200px;height:580px;background:rgba(6,12,24,.55)}
  .footer-title{color:var(--white);font-size:28px;font-weight:400}
  .contact{left:160px;top:3270px;width:260px}
  .contact-row{display:flex;gap:14px;align-items:center;margin-top:30px}
  .contact-icon{width:34px;height:34px;border-radius:50%;background:var(--blue);display:flex;align-items:center;justify-content:center;flex:none}
  .contact-row h4{font-size:13px;color:var(--white);font-weight:700}
  .contact-row p{font-size:10.5px;color:#c7d0de;line-height:1.5}
  .consult{left:470px;top:3270px;width:530px}
  .form{display:grid;grid-template-columns:1fr 1fr;gap:12px 18px;margin-top:26px}
  .field{height:34px;background:rgba(255,255,255,.14);border:1px solid rgba(255,255,255,.2);border-radius:3px;font-size:11px;color:#d6ddea;padding:10px 12px}
  .field.message{grid-column:1/3;height:64px}
  .send-btn{left:480px;top:3620px;width:140px;padding:11px 0;font-size:12px}
  .copyright{left:0;top:3742px;width:1200px;height:38px;background:#06245a;color:#c5d2ea;font-size:11px;text-align:center;line-height:38px}
</style>
</head>
<body>

<!-- hero -->
<div class="abs hero-photo" role="img" aria-label="Photo of a server room with a woman working on a laptop"></div>
<div class="abs hero-shade"></div>
<svg class="abs" style="left:0;top:0" width="1200" height="1020" viewBox="0 0 1200 1020">
  <defs>
    <linearGradient id="heroBlue" x1="0" y1="0" x2="1" y2="1">
      <stop offset="0" stop-color="#7cbcff"/>
      <stop offset="1" stop-color="#2f7ff0"/>
    </linearGradient>
  </defs>
  <path d="M0,770 C260,900 620,940 900,860 C1010,830 1110,790 1200,760 L1200,1020 L0,1020 Z" fill="#ffffff"/>
  <path d="M1200,180 C1050,300 930,450 960,620 C990,800 1100,930 1200,1000 Z" fill="url(#heroBlue)" opacity=".9"/>
  <path d="M1200,420 C1110,520 1070,650 1120,780 C1150,860 1180,900 1200,920 Z" fill="#a9d2ff" opacity=".5"/>
</svg>

<header class="abs nav">
  <div class="brand"><span>TALVIREX GRID</span><span class="brand-dot"></span></div>
  <nav class="nav-links"><span>Home</span><span>Why Us?</span><span>Products</span><span>Resources</span><span>News</span><span>Contact Us</span></nav>
  <span class="btn nav-btn">Get in</span>
</header>

<h1 class="abs hero-title">INDUSTRIAL EDGE COMPUTING<br>PLATFORM</h1>
<p class="abs hero-text">Lorem Ipsum is simply dummy text of the printing and typesetting industry. Lorem Ipsum has been the industry's standard dummy text ever since the 1500s.</p>
<span class="abs btn hero-btn">Free Consulting</span>

<!-- why us -->
<section class="abs why">
  <div class="eyebrow">Internet of Things</div>
  <h2 class="section-title" style="margin-top:6px">Why Us?</h2>
  <div class="title-rule center"></div>
  <p class="body-text">Lorem Ipsum is simply dummy text of the printing and typesetting industry. Lorem Ipsum has been the industry's standard dummy text ever since the 1500s, when an unknown printer took a galley of type and scrambled it to make a type specimen book. It has survived not only five centuries, but also the leap into electronic typesetting, remaining essentially unchanged. It was popularised in the 1960s with the release of Letraset sheets containing Lorem Ipsum passages, and more recently with desktop publishing software like Aldus PageMaker including versions of Lorem Ipsum.</p>
</section>

<div class="abs features">
  <div class="feature">
    <svg width="44" height="44" viewBox="0 0 44 44" fill="none" stroke="#1e3a6b" stroke-width="2"><path d="M12 32h22a7 7 0 0 0 0-14 10 10 0 0 0-19-2A8 8 0 0 0 12 32z"/><path d="M18 38v-6M26 38v-6"/></svg>Cloud</div>
  <div class="feature">
    <svg width="44" height="44" viewBox="0 0 44 44" fill="none" stroke="#1e3a6b" stroke-width="2"><ellipse cx="22" cy="10" rx="13" ry="4"/><path d="M9 10v24c0 2 6 4 13 4s13-2 13-4V10M9 18c0 2 6 4 13 4s13-2 13-4M9 26c0 2 6 4 13 4s13-2 13-4"/></svg>Big Data</div>
  <div class="feature">
    <svg width="44" height="44" viewBox="0 0 44 44" fill="none" stroke="#1e3a6b" stroke-width="2"><rect x="6" y="8" width="32" height="22" rx="2"/><path d="M16 38h12M22 30v8M13 16h8M13 22h14"/></svg>Applications</div>
  <div class="feature">
    <svg width="44" height="44" viewBox="0 0 44 44" fill="none" stroke="#1e3a6b" stroke-width="2"><rect x="12" y="12" width="20" height="20" rx="2"/><rect x="18" y="18" width="8" height="8"/><path d="M17 6v6M22 6v6M27 6v6M17 32v6M22 32v6M27 32v6M6 17h6M6 22h6M6 27h6M32 17h6M32 22h6M32 27h6"/></svg>Pic</div>
  <div class="feature">
    <svg width="44" height="44" viewBox="0 0 44 44" fill="none" stroke="#1e3a6b" stroke-width="2"><rect x="10" y="14" width="24" height="18" rx="3"/><circle cx="17" cy="22" r="2"/><circle cx="27" cy="22" r="2"/><path d="M22 14V8M18 28h8M6 20v6M38 20v6M16 32v6M28 32v6"/><circle cx="22" cy="7" r="1.5"/></svg>Robotic System</div>
  <div class="feature">
    <svg width="44" height="44" viewBox="0 0 44 44" fill="none" stroke="#1e3a6b" stroke-width="2"><circle cx="22" cy="22" r="4"/><path d="M14 14a11 11 0 0 0 0 16M30 14a11 11 0 0 1 0 16M9 9a18 18 0 0 0 0 26M35 9a18 18 0 0 1 0 26"/></svg>Sensors</div>
</div>
<span class="abs btn why-btn">Read More</span>

<!-- resources -->
<svg class="abs" style="left:960px;top:1230px" width="240" height="500" viewBox="0 0 240 500">
  <defs><linearGradient id="resBlue" x1="0" y1="0" x2="1" y2="1"><stop offset="0" stop-color="#8cc4ff"/><stop offset="1" stop-color="#2d7cf0"/></linearGradient></defs>
  <path d="M240,0 C150,40 60,130 50,250 C40,370 140,460 240,500 Z" fill="url(#resBlue)"/>
</svg>
<div class="abs resources-box" role="img" aria-label="Product box packaging with a digital portrait illustration"></div>
<section class="abs resources-copy">
  <div class="eyebrow">Internet of Things</div>
  <h2 class="section-title" style="font-size:30px;margin-top:6px">Resources</h2>
  <div class="title-rule"></div>
  <p class="body-text">Lorem Ipsum is simply dummy text of the printing and typesetting industry. Lorem Ipsum has been the industry's standard dummy text ever since the 1500s, when an unknown printer took a galley of type and scrambled it to make a type specimen book. It has survived not only five centuries, but also the leap into electronic typesetting, remaining essentially unchanged. It was popularised in the 1960s with the release of Letraset sheets containing passages, and more recently with desktop publishing software including versions of Lorem Ipsum.</p>
</section>

<!-- products -->
<svg class="abs" style="left:1000px;top:2120px" width="200" height="440" viewBox="0 0 200 440">
  <defs><linearGradient id="prodBlue" x1="0" y1="0" x2="1" y2="1"><stop offset="0" stop-color="#8cc4ff"/><stop offset="1" stop-color="#2d7cf0"/></linearGradient></defs>
  <path d="M200,0 C120,50 30,140 40,260 C50,350 130,415 200,440 Z" fill="url(#prodBlue)"/>
</svg>
<section class="abs products-copy">
  <div class="eyebrow">Internet of Things</div>
  <h2 class="section-title" style="font-size:30px;margin-top:6px">Our Products</h2>
  <div class="title-rule"></div>
  <p class="body-text">Lorem Ipsum is simply dummy text of the printing and typesetting industry. Lorem Ipsum has been the industry's standard dummy text ever since the 1500s.</p>
  <div class="product-item">
    <svg width="40" height="40" viewBox="0 0 40 40" fill="none" stroke="#f5315c" stroke-width="2"><path d="M10 26h20a6 6 0 0 0 0-12 9 9 0 0 0-17-2A7 7 0 0 0 10 26z"/><path d="M20 26v8M14 34h12"/></svg>
    <div><h3>Talvirex Grid Edge</h3><p>Lorem Ipsum is simply dummy text of the printing and typesetting industry.</p></div>
  </div>
  <div class="product-item">
    <svg width="40" height="40" viewBox="0 0 40 40" fill="none" stroke="#f5315c" stroke-width="2"><rect x="6" y="8" width="28" height="18" rx="2"/><path d="M14 34h12M20 26v8M12 16l5 4 9-7"/></svg>
    <div><h3>Talvirex Grid Edge Manager</h3><p>Lorem Ipsum is simply dummy text of the printing and typesetting industry.</p></div>
  </div>
</section>
<div class="abs products-photo" role="img" aria-label="Photo of an engineer in a hard hat holding a tablet above a connected city skyline"></div>

<!-- latest news -->
<section class="abs news-head">
  <div class="eyebrow">Internet of Things</div>
  <h2 class="section-title" style="margin-top:6px">Latest News</h2>
  <div class="title-rule center"></div>
</section>

<article class="abs news-card" style="left:160px;top:2700px">
  <div class="news-photo" role="img" aria-label="Photo of a team meeting around a table" style="background:linear-gradient(135deg,#c9a27c,#8a6a4f)"></div>
  <div class="news-body"><div class="news-date">24 Jan 2020</div><h3>Lorem ipsum is simply dummy text.</h3><p>Lorem Ipsum is simply dummy text of the printing and typesetting industry. Lorem Ipsum has been the industry's standard dummy text ever since the 1500s, when an unknown printer took a galley.</p></div>
</article>
<article class="abs news-card" style="left:610px;top:2700px">
  <div class="news-photo" role="img" aria-label="Photo of a network device with glowing lights" style="background:linear-gradient(135deg,#1d3d5c,#3c7a8f)"></div>
  <div class="news-body"><div class="news-date">24 Jan 2020</div><h3>Lorem ipsum is simply dummy text.</h3><p>Lorem Ipsum is simply dummy text of the printing and typesetting industry. Lorem Ipsum has been the industry's standard dummy text ever since the 1500s, when an unknown printer took a galley.</p></div>
</article>
<article class="abs news-card" style="left:160px;top:2900px">
  <div class="news-photo" role="img" aria-label="Photo of hands typing on a laptop" style="background:linear-gradient(135deg,#5a5f68,#b8bcc4)"></div>
  <div class="news-body"><div class="news-date">24 Jan 2020</div><h3>Lorem ipsum is simply dummy text.</h3><p>Lorem Ipsum is simply dummy text of the printing and typesetting industry. Lorem Ipsum has been the industry's standard dummy text ever since the 1500s, when an unknown printer took a galley.</p></div>
</article>
<article class="abs news-card" style="left:610px;top:2900px">
  <div class="news-photo" role="img" aria-label="Photo of colleagues working together at a desk" style="background:linear-gradient(135deg,#d8b98e,#6e7f99)"></div>
  <div class="news-body"><div class="news-date">24 Jan 2020</div><h3>Lorem ipsum is simply dummy text.</h3><p>Lorem Ipsum is simply dummy text of the printing and typesetting industry. Lorem Ipsum has been the industry's standard dummy text ever since the 1500s, when an unknown printer took a galley.</p></div>
</article>

<!-- footer -->
<div class="abs footer-photo" role="img" aria-label="Photo of network cables plugged into a blue-lit switch"></div>
<div class="abs footer-shade"></div>

<section class="abs contact">
  <div class="eyebrow">Internet of Things</div>
  <h2 class="footer-title">Contact Info</h2>
  <div class="title-rule"></div>
  <div class="contact-row">
    <span class="contact-icon"><svg width="16" height="16" viewBox="0 0 16 16" fill="#fff"><path d="M8 1a5 5 0 0 0-5 5c0 4 5 9 5 9s5-5 5-9a5 5 0 0 0-5-5zm0 7a2 2 0 1 1 0-4 2 2 0 0 1 0 4z"/></svg></span>
    <div><h4>Address</h4><p>120 Harbor Street, Suite 4<br>Lakeview District</p></div>
  </div>
  <div class="contact-row">
    <span class="contact-icon"><svg width="16" height="16" viewBox="0 0 16 16" fill="#fff"><path d="M4 1l2 3-1.5 1.5a8 8 0 0 0 6 6L12 10l3 2-1 3C7 15 1 9 1 2z"/></svg></span>
    <div><h4>Phone</h4><p>+1 555 0142 7788</p></div>
  </div>
  <div class="contact-row">
    <span class="contact-icon"><svg width="16" height="16" viewBox="0 0 16 16" fill="none" stroke="#fff" stroke-width="1.5"><rect x="1.5" y="3.5" width="13" height="9" rx="1"/><path d="M2 4l6 5 6-5"/></svg></span>
    <div><h4>Email Id</h4><p>hello@talvirexgrid.com</p></div>
  </div>
</section>

<section class="abs consult">
  <div class="eyebrow">Internet of Things</div>
  <h2 class="footer-title">Free Consulting</h2>
  <div class="title-rule"></div>
  <div class="form">
    <div class="field">Name</div>
    <div class="field">Email</div>
    <div class="field">Phone</div>
    <div class="field">Subject</div>
    <div class="field message">Message/comments</div>
  </div>
</section>
<span class="abs btn send-btn">Send Message</span>

<footer class="abs copyright">© 2020 Talvirex Grid. All Rights Reserved. Terms &amp; Conditions</footer>

</body>
</html>
```